Stationery For Upscale Concierge Company

Create stationary that looks good in black and white and uses the attached logo. Needs to be upscale using upscale fonts and layout. Use the attached logo. Reverse out if necessary.

```html
<!DOCTYPE html>
<html lang="en">
<head>
<meta charset="utf-8">
<title>Meridian Concierge Stationery</title>
<link rel="stylesheet" href="https://fonts.googleapis.com/css2?family=Cinzel:wght@400;500&family=Roboto:wght@400;500&family=Great+Vibes&display=swap">
<style>
:root{
  --bg:#d3d3d3;
  --paper:#f1f1f1;
  --ink:#333333;
  --text:#444444;
  --muted:#666666;
  --sig:#2f5b9a;
}
*{margin:0;padding:0;box-sizing:border-box}
html,body{width:1200px;height:848px;overflow:hidden;background:var(--bg)}
body{position:relative;font-family:"Roboto",sans-serif;color:var(--text)}
.sheet{position:absolute;background:var(--paper);overflow:hidden}
.swoosh{position:absolute;top:0;right:0;display:block}
.brand{font-family:"Cinzel",serif;font-weight:500;color:var(--ink);letter-spacing:.06em;white-space:nowrap;display:flex;align-items:center;gap:6px}
.brand .mark{width:7px;height:7px;background:currentColor;display:inline-block}
.brand--light{color:var(--paper)}

/* letterhead */
.letterhead{left:114px;top:146px;width:420px;height:596px}
.letterhead .brand{position:absolute;left:27px;top:57px;font-size:11px}
.letter{position:absolute;left:27px;top:131px;width:368px;font-size:6.6px;line-height:9.7px;color:var(--text)}
.letter .date{margin-bottom:20px}
.letter .addr{margin-bottom:20px}
.letter .addr b{font-weight:500;color:var(--ink)}
.letter p{margin-bottom:9.7px;text-align:justify}
.letter .sign{margin-top:36px}
.letter .sign b{font-weight:500;color:var(--ink)}
.letter .signature{font-family:"Great Vibes",cursive;font-size:14px;line-height:18px;color:var(--sig);margin:0 0 3px -8px}
.footer{position:absolute;left:25px;top:547px;width:370px;display:flex;font-size:5.8px;line-height:8px;color:var(--muted)}
.footer .col{border-left:1px solid var(--ink);padding-left:9px}
.footer .col-brand{width:136px;font-family:"Cinzel",serif;font-size:9.6px;line-height:11px;color:var(--ink);letter-spacing:.05em;font-weight:500}
.footer .col-contact{width:144px}
.contact-line{display:flex;align-items:center;gap:5px}
.contact-line svg{width:5px;height:5px;fill:var(--ink);flex:none}

/* business cards */
.card{top:105px;width:182px;height:110px}
.card--front{left:629px;background:var(--ink);display:flex;align-items:center;justify-content:center}
.card--front .brand{font-size:9.6px}
.card--back{left:848px}
.card--back .brand{position:absolute;left:10px;top:55px;font-size:7.4px}
.card-name{position:absolute;right:10px;top:11px;text-align:right;color:var(--paper)}
.card-name .name{font-family:"Cinzel",serif;font-size:6.8px;letter-spacing:.05em}
.card-name .role{font-size:3.6px;margin-top:1px}
.card-contact{position:absolute;left:10px;top:80px;font-size:4.4px;line-height:6px;color:var(--muted)}
.card-contact svg{width:4px;height:4px}
.card-address{position:absolute;right:10px;top:89px;text-align:right;font-size:4.4px;line-height:6px;color:var(--muted)}

/* envelope front */
.envelope-front{left:574px;top:239px;width:510px;height:229px}
.envelope-front .brand{position:absolute;left:30px;top:85px;font-size:12.5px}
.envelope-contact{position:absolute;left:30px;top:173px;font-size:5.8px;line-height:8px;color:var(--muted)}
.envelope-contact .street{margin-top:3px}

/* envelope back */
.envelope-back{left:576px;top:502px;width:508px;height:229px}
.flap{position:absolute;left:0;top:0;display:block}
.envelope-back .brand{position:absolute;left:0;width:100%;top:25px;justify-content:center;font-size:10px}
.envelope-web{position:absolute;left:0;width:100%;top:201px;text-align:center;font-size:5.6px;letter-spacing:.35em;color:var(--muted)}
</style>
</head>
<body>

<!-- Letterhead -->
<section class="sheet letterhead">
  <svg class="swoosh" width="420" height="62" viewBox="0 0 420 62">
    <path d="M8 0 H420 V54 C300 22 160 6 8 0 Z" fill="var(--ink)"/>
    <path d="M60 1 C200 10 320 28 420 62 L420 58 C320 25 200 8 60 1 Z" fill="var(--ink)"/>
  </svg>
  <div class="brand"><span class="mark"></span>Meridian Concierge</div>

  <div class="letter">
    <div class="date">30/10/2016</div>
    <div class="addr"><b>Mr. R. Halden</b><br>123, Street No. 123,<br>City Name<br>Postcode-123456</div>
    <p style="margin-bottom:14px">Dear Sir,</p>
    <p>Lorem Ipsum is simply dummy text of the printing and typesetting industry. Lorem Ipsum has been the industry's standard dummy text ever since the 1500s, when an unknown printer took a galley of type and scrambled it to make a type specimen book. It has survived not only five centuries, but also the leap into electronic typesetting, remaining essentially unchanged. It was popularised in the 1960s with the release of Transferon sheets containing Lorem Ipsum passages, and more recently with desktop publishing software like Folio PageSetter including versions of Lorem Ipsum.</p>
    <p>Lorem Ipsum is simply dummy text of the printing and typesetting industry. Lorem Ipsum has been the industry's standard dummy text ever since the 1500s, when an unknown printer took a galley of type and scrambled it to make a type specimen book. It has survived not only five centuries, but also the leap into electronic typesetting, remaining essentially unchanged. It was popularised in the 1960s with the release of Transferon sheets containing Lorem Ipsum passages, and more recently with desktop publishing software like Folio PageSetter including versions of Lorem Ipsum.</p>
    <p>Lorem Ipsum is simply dummy text of the printing and typesetting industry. Lorem Ipsum has been the industry's standard dummy text ever since the 1500s, when an unknown printer took a galley of type and scrambled it to make a type specimen book.</p>
    <p>Lorem Ipsum is simply dummy text of the printing and typesetting industry. Lorem Ipsum has been the industry's standard dummy text ever since the 1500s, when an unknown printer took a galley of type and scrambled it to make a type specimen book.</p>
    <div class="sign">
      <b>Your Name</b>
      <div class="signature">Your Signature</div>
      CEO &nbsp;|&nbsp; Owner
    </div>
  </div>

  <div class="footer">
    <div class="col col-brand">Meridian<br>Concierge</div>
    <div class="col col-contact">
      <div class="contact-line"><svg viewBox="0 0 10 10"><path d="M1 2 Q5 -1 9 2 L8 4 L6 3.5 L6 5 H4 V3.5 L2 4 Z M2 5 H8 V9 H2 Z"/></svg>0100-555-010</div>
      <div class="contact-line"><svg viewBox="0 0 10 10"><path d="M0 2 H10 V8 H0 Z"/></svg>alan.grey@example.com</div>
      <div class="contact-line"><svg viewBox="0 0 10 10"><circle cx="5" cy="5" r="4.5"/></svg>www.example.com</div>
    </div>
    <div class="col">58 Linden Row, Marlow<br>4120, Region<br>Postcode - 654321</div>
  </div>
</section>

<!-- Business card front -->
<section class="sheet card card--front">
  <div class="brand brand--light"><span class="mark"></span>Meridian Concierge</div>
</section>

<!-- Business card back -->
<section class="sheet card card--back">
  <svg class="swoosh" width="182" height="60" viewBox="0 0 182 60">
    <path d="M0 0 H182 V36 C130 10 60 30 0 30 Z" fill="var(--ink)"/>
    <path d="M0 34 C60 34 120 14 182 44 V48 C120 20 60 40 0 38 Z" fill="var(--ink)"/>
  </svg>
  <div class="card-name"><div class="name">ALAN GREY</div><div class="role">Managing Director</div></div>
  <div class="brand"><span class="mark"></span>Meridian Concierge</div>
  <div class="card-contact">
    <div class="contact-line"><svg viewBox="0 0 10 10"><path d="M1 2 Q5 -1 9 2 L8 4 L6 3.5 L6 5 H4 V3.5 L2 4 Z M2 5 H8 V9 H2 Z"/></svg>0100-555-010</div>
    <div class="contact-line"><svg viewBox="0 0 10 10"><path d="M0 2 H10 V8 H0 Z"/></svg>alan.grey@example.com</div>
    <div class="contact-line"><svg viewBox="0 0 10 10"><circle cx="5" cy="5" r="4.5"/></svg>www.example.com</div>
  </div>
  <div class="card-address">58 Linden Row, Marlow<br>4120, Postcode - 654321</div>
</section>

<!-- Envelope front -->
<section class="sheet envelope-front">
  <svg class="swoosh" width="510" height="56" viewBox="0 0 510 56">
    <path d="M10 0 H510 V38 C360 16 180 4 10 0 Z" fill="var(--ink)"/>
    <path d="M160 4 C300 12 420 26 510 50 V56 C420 32 300 16 160 4 Z" fill="var(--ink)"/>
  </svg>
  <div class="brand"><span class="mark"></span>Meridian Concierge</div>
  <div class="envelope-contact">
    <div class="contact-line"><svg viewBox="0 0 10 10"><path d="M1 2 Q5 -1 9 2 L8 4 L6 3.5 L6 5 H4 V3.5 L2 4 Z M2 5 H8 V9 H2 Z"/></svg>0100-555-010</div>
    <div class="contact-line"><svg viewBox="0 0 10 10"><path d="M0 2 H10 V8 H0 Z"/></svg>alan.grey@example.com</div>
    <div class="contact-line"><svg viewBox="0 0 10 10"><circle cx="5" cy="5" r="4.5"/></svg>www.example.com</div>
    <div class="street">58 Linden Row, Marlow 4120, With Postcode - 654321</div>
  </div>
</section>

<!-- Envelope back -->
<section class="sheet envelope-back">
  <svg class="flap" width="508" height="64" viewBox="0 0 508 64">
    <path d="M2 0 H506 L478 52 Q472 63 458 63 H52 Q38 63 32 52 Z" fill="var(--ink)"/>
  </svg>
  <div class="brand brand--light"><span class="mark"></span>Meridian Concierge</div>
  <div class="envelope-web">www.example.com</div>
</section>

</body>
</html>
```